Creative Web Design for an ERP (technology) Consulting Business

I need two pages designed for the ERP Project Management Consulting Company I am starting. One page is the home page, the other page is an important inside page.

I've looked at many different templates for sites like this, and they all look the same to me. I am working with ArtForgeHub designers because I want something unique.

This site will be implemented with Wordpress using the Elementor framework,

About Me ---
I have worked with ArtForgeHub several times before, and I have tired to do everything I can to ve helpful. In the uploads, you will find PDF's with wireframes outlning the layout of the pages, as well as explanatios for each section. There are Word documents that you can copy into text. The list below explains the files included.

Although the wireframes suggest a layout, please feel free to use your creativity - often, I find that the designs I like the most are designs I have never thought of.

About the Company --
ERP (Enterprise Resource Planning) systems are business computer systems that tie different businesss functions together. These systems are expensive and complicated, and efforts to implement them often fail. The purpose of the company is to increase the chance of success by focusing on the things that need to be right.

I have uploaded several files to help clarify what I am looking for:
• 1a - Home Page Wireframe - PDF
Wireframe for the home page with an explanation of each section.
• 1b - Home Page Text – Word
A Word document so that you can copy the text.
• 2 - Copper Harbor Logo – ZIP
Four different versions of the company logo in Adobe Illustrator, PNG, and JPG formats. Any of the four are acceptable:
1. Logo_1 – Black on Transparent – Same Line ERP
2. Logo_2 – White on Transparent – Same Line ERP
3. Logo_3 – Black on Transparent – Big ERP on Different Line
4. Logo_4 – White on Transparent – Big ERP on Different Line
• 3a - Copper Harbor Page Wireframe – PDF
Wireframe for he Copper Harbor page, with explanations and a detailed breakdown of the top section.
• 3b - Copper Harbor Text – Word
• 4 - Colors and Palettes – PDF
• 5 - Change Management Icon – EPS
• 6 – Site Map
If you wish to see it, the site map provides an idea of the entire site. The two pages circled in red are the ones I need to be designed.

Thank you for your interest in this project!

Target Market(s)

Corporate decision makers, primarily CIOs and CFOs, as well as ERP project managers and influencers.

Industry/Entity Type

Consulting

Number of Pages Required

2 page

Font styles to use
Sans Serif

Requirements
Must have
• Pages that contain the elements explained on the wireframes provided.
Nice to have
• A design that looks and feels unique
Should not have
• A typical, template layour

```html
<!DOCTYPE html>
<html lang="en">
<head>
<meta charset="utf-8">
<title>Copper Harbor ERP</title>
<link href="https://fonts.googleapis.com/css2?family=Montserrat:wght@700;800;900&family=Poppins:wght@400;500;600&display=swap" rel="stylesheet">
<style>
:root{
  --ink:#1e1f4b;
  --body:#4a4a5a;
  --purple:#3c1f63;
  --purple-card:#4b2b74;
  --violet:#7b3fc9;
  --btn:#5a2590;
  --lilac:#e9e2f5;
  --orange:#f08a1c;
  --white:#ffffff;
}
*{margin:0;padding:0;box-sizing:border-box}
html,body{width:1200px;height:4466px;overflow:hidden}
body{font-family:"Poppins",sans-serif;color:var(--body);background:var(--white);position:relative}
h1,h2,h3,h4{font-family:"Montserrat",sans-serif;color:var(--ink);font-weight:800}
.abs{position:absolute}
.pill{display:inline-block;font-size:13px;padding:4px 18px;border-radius:20px;background:var(--lilac);color:var(--btn)}
.btn{display:inline-block;background:var(--btn);color:#fff;font-size:11px;font-weight:500;padding:9px 20px;border-radius:4px}

/* hero */
.hero{position:absolute;top:0;left:0;width:1200px;height:664px;overflow:hidden;color:#fff}
.hero-bg{position:absolute;inset:0;background:linear-gradient(100deg,#6a4aa8 0%,#3a2a6e 28%,#221c4a 50%,#3a2558 72%,#c8741e 100%)}
.nav{position:absolute;top:55px;left:118px;display:flex;gap:44px;font-size:11px;white-space:nowrap}
.nav a{color:#e6e2f2;text-decoration:none}
.nav a.on{font-weight:600;color:#fff}
.nav-cta{position:absolute;top:47px;left:1027px;width:97px;height:33px;background:#8e4fd6;border-radius:5px;font-size:10px;display:flex;align-items:center;justify-content:center}
.hero-tag{position:absolute;top:168px;left:402px;background:rgba(255,255,255,.12);color:#f3a84a;font-size:10px;padding:4px 14px;border-radius:14px}
.hero h1{position:absolute;top:204px;left:402px;width:760px;color:#fff;font-size:30px;line-height:40px}
.hero-label{position:absolute;font-size:12.5px;font-weight:500;display:flex;gap:8px;line-height:18px;white-space:nowrap}
.hub{position:absolute;left:640px;top:445px;width:200px;height:112px;background:#2e2b3f;border-radius:8px;display:flex;align-items:center;justify-content:center;gap:8px}
.hub span{font-family:"Poppins",sans-serif;font-weight:600;font-size:15px;color:#fff;white-space:nowrap}
.hub i{width:12px;height:12px;border-radius:50%;background:#e24b5a}

/* about */
.about{position:absolute;top:664px;left:0;width:1200px;height:631px}
.about .pill{position:absolute;top:82px;left:112px}
.about h2{position:absolute;top:114px;left:112px;font-size:38px;white-space:nowrap}
.about-copy{position:absolute;top:200px;left:112px;width:480px;font-size:13px;line-height:24px}
.about-copy h4{font-size:17px;margin:26px 0 8px}
.about-photo{position:absolute;left:718px;top:100px;width:345px;height:400px;border-radius:30px;background:linear-gradient(160deg,#6b6a86,#3d3a5c 60%,#2a2746)}
.about-frame{position:absolute;left:702px;top:84px;width:377px;height:430px;border:3px solid #d8cdee;border-radius:38px}
.widget{position:absolute;background:#fff;border-radius:12px;box-shadow:0 8px 24px rgba(40,20,80,.15)}
.play{position:absolute;width:60px;height:60px;border-radius:50%;background:rgba(120,70,200,.75);display:flex;align-items:center;justify-content:center}

/* pillars */
.pillars{position:absolute;top:1295px;left:0;width:1200px;height:730px;background:var(--purple)}
.pcard{position:absolute;top:60px;width:490px;height:605px;background:var(--purple-card);border-radius:28px;padding:34px 34px 0;color:#e4dcf2}
.pcard .pill{background:rgba(255,255,255,.18);color:#e9e0f7;font-size:12px;padding:3px 24px}
.pcard h2{color:#fff;font-size:40px;margin:8px 0 26px;white-space:nowrap}
.pcard p{font-size:13px;line-height:24px;margin-bottom:10px}
.video{position:absolute;left:34px;bottom:34px;width:420px;height:270px;border-radius:22px;overflow:hidden}
.video .cap{position:absolute;left:28px;bottom:22px;color:#fff;font-size:12px;display:flex;gap:10px;align-items:center}

/* services */
.services{position:absolute;top:2025px;left:0;width:1200px;height:1436px}
.center{text-align:center;width:1200px;position:absolute;left:0}
.svc-img{position:absolute;width:305px;height:200px;border-radius:22px}
.svc-frame{position:absolute;width:330px;height:225px;border:2px solid #cfc3e6;border-radius:30px}
.svc-text{position:absolute;width:460px;font-size:11px;line-height:20px}
.svc-text h3{font-size:22px;margin-bottom:8px}
.svc-text b{display:block;color:var(--ink);font-weight:600;margin-bottom:18px}
.svc-text p{margin-bottom:18px}

/* experience */
.experience{position:absolute;top:3461px;left:0;width:1200px;height:605px;background:linear-gradient(180deg,#3f2366,#33195a)}
.experience .pill{background:rgba(255,255,255,.14);color:#e9e0f7}
.side{position:absolute;top:334px;width:295px;height:94px;background:#fff;display:flex;align-items:center}
.side h4{font-size:17px;line-height:22px;width:140px}
.xcard{position:absolute;left:322px;top:239px;width:554px;height:280px;background:#fff;display:flex}
.xcard .txt{padding:34px 24px 0 26px;font-size:11px;line-height:20px;flex:1}
.xcard h3{font-size:22px;margin-bottom:12px}

/* subscribe */
.subscribe{position:absolute;top:4066px;left:0;width:1200px;height:238px;overflow:hidden}
.sub-img{position:absolute;right:0;top:0;width:640px;height:238px;clip-path:polygon(8% 0,100% 0,100% 100%,0 100%);background:linear-gradient(110deg,#c8d2ee,#7a8fd0 45%,#5a3a9e)}
.subscribe h2{position:absolute;left:100px;top:82px;font-size:40px}
.sub-form{position:absolute;left:100px;top:142px;display:flex;gap:16px}
.sub-form .in{width:322px;height:36px;border:1px solid #999;font-size:11px;padding:10px}
.sub-form .go{height:36px;width:112px;border:1px solid var(--ink);font-size:11px;display:flex;align-items:center;justify-content:center;color:var(--ink)}

/* footer */
.footer{position:absolute;top:4304px;left:0;width:1200px;height:162px}
.fcol{position:absolute;top:30px;font-size:11px;line-height:23px}
.fcol h4{font-size:17px;margin-bottom:10px}
.fcol li{list-style:none;padding-left:16px;position:relative}
.fcol li:before{content:"";position:absolute;left:0;top:10px;width:5px;height:5px;border-radius:50%;background:#c7bcdd}
</style>
</head>
<body>

<section class="hero">
  <div class="hero-bg" role="img" aria-label="Team of business professionals standing in an office, blended into a purple to orange gradient"></div>
  <nav class="nav">
    <a class="on">Home</a><a>About</a><a>Services</a><a>Copper Harbor</a><a>Anchor Route</a><a>Resources</a><a>Case Studies</a><a>Contact Us</a>
  </nav>
  <div class="nav-cta">Contact Us</div>
  <div class="hero-tag">We Can Help You With ERP</div>
  <h1>Decades In Pursuit Of Excellence In Enterprise Applications Informed By A Researched Approach To ERP Success</h1>
  <svg class="abs" style="left:560px;top:420px" width="360" height="170" fill="none" stroke="#c9c4d8" stroke-width="1.5">
    <path d="M12 8 H40 Q52 8 52 22 V36 Q52 48 66 48 H80"/>
    <path d="M0 150 H38 Q52 150 52 136 V124 Q52 112 66 112 H80"/>
    <path d="M348 8 H320 Q308 8 308 22 V36 Q308 48 294 48 H280"/>
    <path d="M348 150 H322 Q308 150 308 136 V124 Q308 112 294 112 H280"/>
  </svg>
  <div class="hero-label" style="left:435px;top:420px">▣ Project Planning</div>
  <div class="hero-label" style="left:408px;top:565px">▣ Project Management</div>
  <div class="hero-label" style="left:915px;top:415px">▣ <span>Project Assessments<br>And Turnaround</span></div>
  <div class="hero-label" style="left:915px;top:564px">▣ Change Management</div>
  <div class="hub"><i></i><span>Copper Harbor ERP</span></div>
</section>

<section class="about">
  <span class="pill">ⓘ About</span>
  <h2>Hi! I’m Daniel Morrow</h2>
  <div class="about-copy">
    <p>Hi! I’m Daniel Morrow, A Consultant And ERP Leader With Extensive Experience In ERP Project Management. My Journey Is Shaped By Experience, Lifelong Learning, And A Commitment To Excellence.</p>
    <h4>Looking For Information?</h4>
    <p>This Site Shares Information Related To Successful ERP Implementations Within A Framework And Method Based On “Whys.”</p>
    <h4>Looking For Help?</h4>
    <p>My Purpose Is To Help Organizations Maximize The Transformational Value Of ERP Systems While Minimizing Organizational Pain And Damage. My Approach Is The Result Of Years Of Research Into What It Takes To Be Successful In ERP Implementations, Supported By Real-World Experience.</p>
  </div>
  <div class="about-frame"></div>
  <div class="about-photo" role="img" aria-label="Consultant working on a laptop at a desk"></div>
  <div class="play" style="left:845px;top:270px"><svg width="20" height="20"><circle cx="10" cy="10" r="10" fill="#fff"/><path d="M8 6 L14 10 L8 14Z" fill="#5a2590"/></svg></div>
  <div class="widget" style="left:660px;top:200px;width:105px;height:100px">
    <svg width="105" height="100"><path d="M25 62 A28 28 0 1 1 80 62" stroke="#e6e0f2" stroke-width="8" fill="none"/><path d="M25 62 A28 28 0 0 1 60 30" stroke="#5a2590" stroke-width="8" fill="none"/><circle cx="52" cy="62" r="5" fill="#7b3fc9"/></svg>
  </div>
  <div class="widget" style="left:1010px;top:265px;width:108px;height:108px">
    <svg width="108" height="108"><circle cx="24" cy="30" r="8" stroke="#3a6fd8" stroke-width="3" fill="none"/><rect x="40" y="26" width="40" height="3" fill="#ccc"/><circle cx="24" cy="56" r="8" stroke="#c04ac8" stroke-width="3" fill="none"/><rect x="40" y="52" width="40" height="3" fill="#ccc"/><circle cx="24" cy="82" r="8" stroke="#f08a1c" stroke-width="3" fill="none"/><rect x="40" y="78" width="40" height="3" fill="#ccc"/></svg>
  </div>
  <div class="widget" style="left:830px;top:456px;width:108px;height:108px">
    <svg width="108" height="108"><circle cx="54" cy="54" r="26" stroke="#e2e2e6" stroke-width="12" fill="none"/><path d="M54 28 A26 26 0 0 1 80 54" stroke="#bdbdc6" stroke-width="12" fill="none"/></svg>
  </div>
</section>

<section class="pillars">
  <div class="pcard" style="left:85px">
    <span class="pill">ERP Framework</span>
    <h2>Copper Harbor</h2>
    <p>The Number Of Things You Need To Do In An ERP Implementation Boggles The Mind.</p>
    <p>It Starts With <b>‘why.’</b> Copper Harbor Groups Hundreds Of Critical Success Factors Into Recurring Themes, Distilling Them Into High-Level Categories That Drive Success. Copper Harbor Simplifies Complexity While Retaining Essential Details.</p>
    <div class="video" role="img" aria-label="Business people reviewing documents and a tablet" style="background:linear-gradient(135deg,#5c5a6e,#2a2438 70%)">
      <div class="play" style="right:22px;bottom:22px;left:auto;width:80px;height:80px"><svg width="34" height="34"><circle cx="17" cy="17" r="17" fill="#fff"/><path d="M13 10 L24 17 L13 24Z" fill="#5a2590"/></svg></div>
      <div class="cap">▭ Copper Harbor ERP Framework</div>
    </div>
  </div>
  <div class="pcard" style="left:617px">
    <span class="pill" style="background:#7a4a3a;color:#f3a84a">Method</span>
    <h2>Anchor Route</h2>
    <p>The Copper Harbor Are The <b>Why</b> And <b>What.</b> Anchor Route Is The <b>How, When,</b> And <b>Who.</b></p>
    <p>Anchor Route, Drawing From The Principles Of Waterfall Planning And Agile Execution, Is Designed To Be Adaptable. It Can Be Overlaid On Any Methodology, Giving You The Confidence That All Critical Elements Will Be Addressed.</p>
    <div class="video" role="img" aria-label="Businessman with a rising growth arrow chart" style="background:linear-gradient(135deg,#2d4a74,#1d2840 70%)">
      <div class="play" style="right:22px;bottom:8px;left:auto;width:80px;height:80px;background:var(--orange)"><svg width="34" height="34"><circle cx="17" cy="17" r="17" fill="#fff"/><path d="M13 10 L24 17 L13 24Z" fill="#f08a1c"/></svg></div>
      <div class="cap">▭ Anchor Route Method</div>
    </div>
  </div>
</section>

<section class="services">
  <div class="center" style="top:66px"><span class="pill">How Can We Help You?</span></div>
  <h2 class="center" style="top:98px;font-size:40px">Services</h2>

  <div class="svc-frame" style="left:185px;top:215px"></div>
  <div class="svc-img" style="left:198px;top:228px;background:linear-gradient(135deg,#8f8cb8,#4a3f80)" role="img" aria-label="Hand writing on sticky notes on a glass board"></div>
  <div class="svc-text" style="left:555px;top:222px">
    <h3>Project Planning</h3>
    <b>“Failing To Plan Is Planning To Fail” - Elias Thornbury<br>“Everybody Has A Plan Until They Get Punched In The Face” - Marco Delgado</b>
    <p>Both Of These Quotes Are True, And Resolving This Paradox Is Essential To Success. I Can Help You Develop A Plan Based On Your Current Situation And Your Desired Future State.</p>
    <span class="btn">Read more</span>
  </div>

  <div class="svc-text" style="left:185px;top:520px">
    <h3>Project Management</h3>
    <b>Project “Management” Is Not Just About Management, It’s About Leadership. Both Are Essential.</b>
    <p>With My Extensive Career Spent Leading Business Application Implementations, I Bring A Wealth Of Experience To The Table. You Can Trust Me To Guide You Through Your Implementation Process With Confidence And Expertise.</p>
    <span class="btn">Read more</span>
  </div>
  <div class="svc-frame" style="left:682px;top:512px"></div>
  <div class="svc-img" style="left:695px;top:525px;background:linear-gradient(135deg,#7b82b0,#2e2c62)" role="img" aria-label="Presenter leading a meeting in a glass office"></div>

  <div class="svc-frame" style="left:185px;top:818px"></div>
  <div class="svc-img" style="left:198px;top:831px;background:linear-gradient(135deg,#3a3a6a,#1d1a45)" role="img" aria-label="Hand touching a digital interface"></div>
  <div class="svc-text" style="left:555px;top:818px">
    <h3>Project Assessments And<br>Turnaround</h3>
    <b>If Your Project Has Gone Off Track, I Can Help You Get It Back On The Rails.</b>
    <p>It Starts With Knowing What You Need To Do Right, And A Process For Identifying What’s Gone Wrong. Copper Harbor Provides The Details Of What Needs To ‘go Right’, And The Copper Harbor Assessment Provides Guidance On What’s Going Wrong.</p>
    <span class="btn">Read more</span>
  </div>

  <div class="svc-text" style="left:185px;top:1138px">
    <h3>Change Management</h3>
    <b>ERP Implementations Represent Major Change Across Many Different Dimensions, And Change Is Hard.</b>
    <p>So Hard That I Went Back To School To Study Industrial/Organizational Psychology To Better Understand Why It Is So Hard, And A ChangeCert Certification In Change Management To Make It Easier. I Can Help You Navigate These Turbulent Waters.</p>
    <span class="btn">Read more</span>
  </div>
  <div class="svc-frame" style="left:682px;top:1132px"></div>
  <div class="svc-img" style="left:695px;top:1145px;background:linear-gradient(135deg,#a8a6c4,#3d3470)" role="img" aria-label="Hand stopping a row of falling dominoes"></div>
</section>

<section class="experience">
  <div class="center" style="top:76px"><span class="pill">We Offer The Best</span></div>
  <h2 class="center" style="top:110px;font-size:40px;color:#fff">Experience</h2>
  <div class="side" style="left:0;padding-left:36px"><h4>Change Management</h4>
    <div role="img" aria-label="Business team meeting" style="position:absolute;right:0;top:0;width:115px;height:94px;background:linear-gradient(135deg,#a8b6d8,#5a6aa0)"></div></div>
  <div class="side" style="left:905px"><div role="img" aria-label="Business team meeting" style="width:115px;height:94px;background:linear-gradient(135deg,#a8b6d8,#5a6aa0)"></div><h4 style="margin-left:52px">Stratavue</h4></div>
  <div class="xcard">
    <div role="img" aria-label="Modern glass office towers viewed from below" style="width:208px;height:280px;background:linear-gradient(160deg,#e8ecf4,#8a96b8 60%,#4a5478)"></div>
    <div class="txt">
      <h3>Enterprise Systems</h3>
      <p>Lorem Ipsum Dolor Sit Amet, Consectetur Adipiscing Elit, Sed Do Eiusmod Tempor Incididunt Ut Labore Et Dolore Magna Aliqua. Ut Enim Ad Minim Veniam, Quis Nostrud Exercitation Ullamco Laboris Nisi Ut Aliquip Ex Ea Commodo Consequat. Duis Aute Irure Dolor In Reprehenderit In Voluptate Velit Esse Cillum Dolore Eu Fugiat Nulla Pariatur. Excepteur Sint Occaecat</p>
      <div style="text-align:center;margin-top:16px"><span class="btn" style="background:var(--purple);padding:9px 22px">Discover more</span></div>
    </div>
  </div>
</section>

<section class="subscribe">
  <div class="sub-img" role="img" aria-label="Silhouettes of business people walking in a bright city setting"></div>
  <span class="pill abs" style="left:100px;top:40px">For Updates</span>
  <h2>Subscribe</h2>
  <div class="sub-form"><div class="in">Enter Your Email</div><div class="go">Join Us Today</div></div>
</section>

<footer class="footer">
  <div class="fcol" style="left:100px"><h4>ERP Tools</h4><ul><li>Copper Harbor</li><li>Anchor Route Method</li><li>Tools And Resources</li></ul></div>
  <div class="fcol" style="left:437px"><h4>Services</h4><ul><li>About</li><li>Project Planning</li><li>Project Management</li></ul></div>
  <div class="fcol" style="left:598px;top:66px;line-height:17px"><ul><li>Project Assessment<br>And Turnaround</li><li style="margin-top:6px">Change Management</li></ul></div>
  <div class="fcol" style="left:935px"><h4>Contact</h4>
    <div>✉&nbsp;&nbsp; dmorrow@copperharborerp</div>
    <div>☏&nbsp;&nbsp; (555) 014-2290</div>
  </div>
</footer>

</body>
</html>
```